Potential SF Gazette Best Seller Poetry Book Cover Contest

I’m penning my first poetry book. It’s entitled “Lanterns Under Rain”
I’m fairly open to creative freedom but I want the cover to without a doubt catch a persons' eye instantly because first impressions are VERY IMPORTANT in the literary world
I tend to lean towards a luxury look and colors like black, gold, rose gold, silver, glitter etc but again I’m open to interpretation
Looking forward to your submissions
Target Market(s)
those seeking relatable love advice and quotes
modern millenials
Colors
Look and feel

```html
<!DOCTYPE html>
<html lang="en">
<head>
<meta charset="UTF-8">
<title>Lanterns Under Rain — Book Cover</title>
<link href="https://fonts.googleapis.com/css2?family=Special+Elite&family=EB+Garamond:ital@1&display=swap" rel="stylesheet">
<style>
  :root {
    --page: #ffffff;
    --cream: #ebe4c4;
    --navy: #0a2b3c;
    --coral: #e87268;
  }
  html, body {
    margin: 0;
    padding: 0;
    width: 1200px;
    height: 1200px;
    overflow: hidden;
    background: var(--page);
  }
  .canvas {
    position: relative;
    width: 1200px;
    height: 1200px;
    background: var(--page);
  }
  .cover {
    position: absolute;
    left: 276px;
    top: 83px;
    width: 648px;
    height: 1034px;
    background: var(--cream);
    overflow: hidden;
  }
  .cover-art {
    position: absolute;
    left: 185px;
    top: 206px;
    width: 311px;
    height: 784px;
    border-radius: 46% 46% 14% 14% / 28% 28% 8% 8%;
    background: linear-gradient(180deg, var(--coral) 0%, var(--coral) 58%, var(--navy) 78%, var(--navy) 100%);
  }
  .title-line {
    position: absolute;
    margin: 0;
    font-family: "Special Elite", "Courier New", monospace;
    font-size: 68px;
    line-height: 1;
    color: var(--navy);
    white-space: nowrap;
    z-index: 2;
  }
  .title-line--1 { right: 171px; top: 62px; }
  .title-line--2 { right: 63px; top: 129px; }
  .title-line--3 { right: 63px; top: 193px; }
  .byline-line {
    position: absolute;
    margin: 0;
    font-family: "EB Garamond", Georgia, serif;
    font-style: italic;
    font-size: 40px;
    line-height: 1;
    color: var(--navy);
    white-space: nowrap;
    z-index: 2;
  }
  .byline-line--genre { left: 43px; top: 486px; }
  .byline-line--by { left: 142px; top: 555px; }
  .byline-line--first { left: 102px; top: 620px; }
  .byline-line--last { left: 48px; top: 686px; }
</style>
</head>
<body>
  <div class="canvas">
    <section class="cover">
      <div class="cover-art" role="img" aria-label="Illustration of an anatomical heart dripping ink into an ink jar"></div>
      <h1 class="book-title">
        <span class="title-line title-line--1">lanterns</span>
        <span class="title-line title-line--2">under</span>
        <span class="title-line title-line--3">rain</span>
      </h1>
      <p class="byline">
        <span class="byline-line byline-line--genre">poetry</span>
        <span class="byline-line byline-line--by">by</span>
        <span class="byline-line byline-line--first">marlow</span>
        <span class="byline-line byline-line--last">quinn-aster</span>
      </p>
    </section>
  </div>
</body>
</html>
```